Business card and stationary package

Travel management company looking for designs for single sided business cards, letterhead and envelope. Looking for contemporary designs using our existing logo. Design should clean, not trendy, no gradation of colors and no graphic other than the icon from the logo. Nothing complicated or difficult to read. Should be a crisp design using blue, gray and black colors only.
Letterhead should include a Word template and PDF template.
Business cards are one sided as the reverse will be dynamic images in our company portfolio of images.
We will use the same designer periodically for design projects using the same style guide for upcoming projects as well. Prefer working with designer that will assist with website, brochures and other marketing materials.

Logo Colors and Font:
Blue: 2189c6 Color Hex
Gray: 666666 Color Hex 60% Black
Black: 100% Black
Font: Century Gothic

Target Market(s)

business-to-business

Industry/Entity Type

Travel Industry

Contact Information for Business Card

Sample information for business cards will be:

Daniel Fenwick
Managing Partner

Harborline Journey Services, Inc.
274 Alder Lane, Suite 3621
Tolland, ME 04123

207-555-0148 Direct Dial
207-555-0193 Fax

daniel@harborlinejourney.net
www.harborlinejourney.net

Font styles to use
Sans Serif

Requirements
Must have
• Clean, crisp design, easy to ready, memorable.
Nice to have
• We tend to like dynamic designs that are simple, not trendy, contemporary and easy to read.
Should not have
• no gradation of colors and no graphic other than the icon from the logo, no background images
• **Note that the background should only be white. No black/gary backgrounds or graded colors**

```html
<!DOCTYPE html>
<html lang="en">
<head>
<meta charset="utf-8">
<title>Harborline Stationery</title>
<link href="https://fonts.googleapis.com/css2?family=Questrial&family=Arimo:wght@400;700&display=swap" rel="stylesheet">
<style>
:root{
  --blue:#2189c6;
  --gray:#666666;
  --black:#000000;
  --ink:#1a1a1a;
  --paper:#ffffff;
  --backdrop:#e2e3e5;
  --flap-line:#c9cacd;
  --signature-fill:#e4e4e4;
}
*{margin:0;padding:0;box-sizing:border-box}
html,body{width:1200px;height:900px;overflow:hidden;background:var(--backdrop)}
.canvas{position:relative;width:1200px;height:900px}
.sheet{position:absolute;background:var(--paper);box-shadow:0 1px 2px rgba(0,0,0,.12)}
.brand{position:absolute;display:flex;align-items:center;gap:8px;font-family:"Questrial",sans-serif;color:var(--gray);letter-spacing:.04em;white-space:nowrap}
.brand-dot{border-radius:50%;background:var(--blue);flex:none}

/* letterhead */
.letterhead{left:64px;top:103px;width:534px;height:691px}
.letterhead .brand{left:44px;top:58px;font-size:30px}
.letterhead .brand-dot{width:26px;height:26px}
.recipient{position:absolute;left:44px;top:166px;font-family:"Arimo",sans-serif;font-size:9px;line-height:11px;color:var(--ink)}
.recipient strong{display:block;font-size:11px;margin-bottom:4px}
.body-copy{position:absolute;left:44px;top:259px;width:456px;font-family:"Arimo",sans-serif;font-size:9.6px;line-height:15.6px;color:var(--ink);letter-spacing:-.2px}
.body-copy p{margin-bottom:15.6px}
.closing{position:absolute;left:44px;top:476px;font-family:"Arimo",sans-serif;font-size:10px;color:var(--ink)}
.signature{position:absolute;left:44px;top:500px;width:122px;height:38px;background:var(--signature-fill);border-radius:3px}
.signer{position:absolute;left:44px;top:542px;font-family:"Arimo",sans-serif;font-size:10px;line-height:13px;color:var(--ink)}
.signer strong{display:block;font-size:11px}
.footer-rule{position:absolute;left:46px;top:624px;width:443px;height:3px;background:var(--blue)}
.footer{position:absolute;left:55px;top:636px;display:flex;align-items:flex-start;font-family:"Questrial",sans-serif;font-size:9.6px;line-height:10.5px;color:var(--gray)}
.footer .col{display:flex;flex-direction:column}
.footer .divider{width:2px;height:20px;background:var(--blue);margin:0 30px}
.line{display:flex;align-items:center;gap:4px}
.ico{width:8px;height:8px;background:var(--blue);border-radius:1px;flex:none}

/* envelope front */
.envelope-front{left:656px;top:102px;width:470px;height:235px}
.envelope-front .brand{left:22px;top:38px;font-size:22px}
.envelope-front .brand-dot{width:20px;height:20px}
.return-address{position:absolute;left:22px;top:188px;font-family:"Questrial",sans-serif;font-size:8.4px;line-height:10px;color:var(--gray)}

/* envelope back */
.envelope-back{left:656px;top:355px;width:470px;height:235px}
.flap{position:absolute;left:0;top:0}
.flap-dot{position:absolute;left:220px;top:19px;width:28px;height:28px;border-radius:50%;background:var(--blue)}

/* business card */
.card{left:778px;top:663px;width:226px;height:129px}
.card .brand{left:46px;top:32px;font-size:17px}
.card .brand-dot{width:16px;height:16px}
.card-person{position:absolute;right:124px;top:79px;text-align:right;font-family:"Questrial",sans-serif;font-size:6px;line-height:7.2px;color:var(--gray)}
.card-person .name{font-size:9.5px;line-height:10px;color:var(--blue)}
.card-person .title{color:var(--ink);margin-bottom:3px}
.card-rule{position:absolute;left:109px;top:80px;width:1px;height:33px;background:var(--blue)}
.card-contact{position:absolute;left:117px;top:79px;font-family:"Questrial",sans-serif;font-size:6px;line-height:8px;color:var(--gray)}
.card-contact .ico{width:6px;height:6px}
</style>
</head>
<body>
<div class="canvas">

  <section class="sheet letterhead">
    <div class="brand"><span class="brand-dot"></span>HARBORLINE</div>
    <div class="recipient"><strong>CLARA WHITMORE</strong>Street Name,City Name.<br>Zip Coad 0000</div>
    <div class="body-copy">
      <p>Lorem Ipsum is simply dummy text of the printing and typesetting industry. Lorem Ipsum has been the industry's standard dummy text ever since the 1500s, when an unknown printer took a galley of type and scrambled it to make a type specimen book. It has survived not only five centuries, but also the leap into electronic typesetting, remaining essentially unchanged. It was popularised in the 1960s with the release of Letraset sheets containing Lorem Ipsum passages, and more recently with desktop publishing software like Aldus PageMaker including versions of Lorem Ipsum.</p>
      <p>It is a long established fact that a reader will be distracted by the readable content of a page when looking at its layout. The point of using Lorem Ipsum is that it has a more-or-less normal distribution of letters, as opposed to using 'Content here, content here', making it look like readable English. Many desktop years, sometimes by accident, sometimes on purpose (injected humour and the like).</p>
    </div>
    <div class="closing">Regards,</div>
    <div class="signature" role="img" aria-label="Handwritten signature of Martin Hale"></div>
    <div class="signer"><strong>Martin Hale</strong>General Maneger</div>
    <div class="footer-rule"></div>
    <div class="footer">
      <div class="col">
        <span class="line"><span class="ico"></span>207-555-0148</span>
        <span class="line"><span class="ico"></span>207-555-0193</span>
      </div>
      <span class="divider"></span>
      <div class="col">
        <span class="line"><span class="ico"></span>www.harborlinejourney.net</span>
        <span class="line"><span class="ico"></span>daniel@harborlinejourney.net</span>
      </div>
      <span class="divider"></span>
      <div class="col">
        <span>274 Alder Lane, Suite 3621</span>
        <span>Tolland, ME 04123</span>
      </div>
    </div>
  </section>

  <section class="sheet envelope-front">
    <div class="brand"><span class="brand-dot"></span>HARBORLINE</div>
    <div class="return-address">Harborline Journey Services, Inc.<br>274 Alder Lane, Suite 3621<br>Tolland, ME 04123</div>
  </section>

  <section class="sheet envelope-back">
    <svg class="flap" width="470" height="70" viewBox="0 0 470 70">
      <path d="M1 1 L8 58 Q9 65 17 65 L453 65 Q461 65 462 58 L469 1" fill="none" stroke="#c9cacd" stroke-width="1.2"/>
    </svg>
    <span class="flap-dot"></span>
  </section>

  <section class="sheet card">
    <div class="brand"><span class="brand-dot"></span>HARBORLINE</div>
    <div class="card-person">
      <div class="name">Daniel Fenwick</div>
      <div class="title">Managing Partner</div>
      <div>274 Alder Lane, Suite 3621</div>
      <div>Tolland, ME 04123</div>
    </div>
    <div class="card-rule"></div>
    <div class="card-contact">
      <div class="line"><span class="ico"></span>207-555-0148</div>
      <div class="line"><span class="ico"></span>207-555-0193</div>
      <div class="line"><span class="ico"></span>daniel@harborlinejourney.net</div>
      <div class="line"><span class="ico"></span>www.harborlinejourney.net</div>
    </div>
  </section>

</div>
</body>
</html>
```